Halvering & Partners, LLC Business Card 2016

We need a new business card design for a very important trade show coming up.

We are a compliance Consulting Firm. Our clients are stock brokerage firms and investment advisers.

I would like our logo on both sides of the card.

Info in the front of the card shold include:

Logo
First & Last Name
Title
Office #
Cell #
Email
Company Address (42 W. Calloway Blvd., Suite 300 Larkmont, CA 91847

Back of the card should include the logo and url: www.halveringpartnersgroup.com

Target Market(s)

Stock Brokerage Firms and Investment Advisers

Industry/Entity Type

Financial Service

Contact Information for Business Card

Russell K. Halvering
President
42 W. Calloway Blvd., Suite 300
Larkmont, CA 91847
O 555.555.0147 ext. 204
C 555.555.0192
Email: russ@halveringpartnersgroup.com
www.halveringpartnersgroup.com

Requirements
Nice to have
• The back of the card could be black with the logo with the white letters.
• I do want the front of the card to at least have the color logo with the black "Halvering & Partners Lettering.

```html
<!DOCTYPE html>
<html lang="en">
<head>
<meta charset="utf-8">
<title>Halvering &amp; Partners – Business Card</title>
<link rel="stylesheet" href="https://fonts.googleapis.com/css2?family=Arimo:wght@400;700&display=swap">
<style>
  :root {
    --frame-red: #8c0f10;
    --bright-red: #e3262b;
    --deep-red: #6a0708;
    --panel-black: #050505;
    --panel-grey: #ebebec;
    --ink-white: #ffffff;
    --ink-black: #111111;
    --page: #ffffff;
  }
  * { box-sizing: border-box; margin: 0; padding: 0; }
  html, body { width: 847px; height: 1200px; overflow: hidden; background: var(--page); }
  body { position: relative; font-family: "Arimo", Arial, sans-serif; }

  .card { position: absolute; left: 14px; width: 829px; overflow: hidden; }
  .card-front { top: 14px; height: 454px; }
  .card-back { top: 592px; height: 482px; }
  .card-art { position: absolute; inset: 0; width: 100%; height: 100%; }

  .contact { position: absolute; left: 16px; top: 20px; color: var(--ink-white); }
  .contact-name { font-size: 37px; font-weight: 400; line-height: 1; letter-spacing: 0.2px; }
  .contact-name strong { font-weight: 700; }
  .contact-title { margin-top: 10px; font-size: 21px; }
  .contact-lines { position: absolute; left: 16px; font-size: 22px; line-height: 26px; color: var(--ink-white); }
  .address { top: 244px; }
  .phones { top: 324px; }
  .email { top: 408px; }

  .wordmark { position: absolute; display: flex; flex-direction: column; align-items: center; font-family: "Arimo", Arial, sans-serif; font-weight: 700; text-transform: uppercase; }
  .wordmark-square { background: var(--bright-red); }
  .wordmark-name { line-height: 1; white-space: nowrap; }
  .wordmark-sub { line-height: 1; white-space: nowrap; }

  .card-front .wordmark { left: 586px; width: 236px; top: 142px; color: var(--ink-black); }
  .card-front .wordmark-square { width: 52px; height: 52px; margin-bottom: 14px; }
  .card-front .wordmark-name { font-size: 32px; letter-spacing: 1px; }
  .card-front .wordmark-sub { font-size: 13px; letter-spacing: 4px; margin-top: 6px; }

  .card-back .wordmark { left: 0; width: 829px; top: 72px; color: var(--ink-white); }
  .card-back .wordmark-square { width: 90px; height: 90px; margin-bottom: 22px; }
  .card-back .wordmark-name { font-size: 58px; letter-spacing: 2px; }
  .card-back .wordmark-sub { font-size: 20px; letter-spacing: 9px; margin-top: 8px; }

  .web-address { position: absolute; left: 0; width: 829px; top: 438px; text-align: center; font-size: 24px; font-weight: 700; color: var(--ink-black); letter-spacing: 0.3px; }
</style>
</head>
<body>

<section class="card card-front" aria-label="Card front">
  <svg class="card-art" viewBox="0 0 829 454" aria-hidden="true">
    <defs>
      <linearGradient id="frontRed" x1="0" y1="0" x2="1" y2="1">
        <stop offset="0" stop-color="var(--deep-red)"/>
        <stop offset="0.5" stop-color="var(--bright-red)"/>
        <stop offset="1" stop-color="var(--deep-red)"/>
      </linearGradient>
      <linearGradient id="swoosh" x1="0" y1="0" x2="1" y2="0">
        <stop offset="0" stop-color="var(--deep-red)"/>
        <stop offset="0.6" stop-color="var(--bright-red)"/>
        <stop offset="1" stop-color="#ff4a4a"/>
      </linearGradient>
    </defs>
    <rect width="829" height="454" fill="url(#frontRed)"/>
    <path d="M565 0 C530 120 600 300 575 454 L600 454 C575 300 545 140 600 0 Z" fill="url(#swoosh)"/>
    <path d="M7 7 H543 C520 140 560 300 531 447 H7 Z" fill="var(--panel-black)"/>
    <path d="M604 7 H822 V447 H578 C600 330 520 220 604 7 Z" fill="var(--panel-grey)"/>
  </svg>

  <div class="contact">
    <h1 class="contact-name">RUSSELL K. <strong>HALVERING</strong></h1>
    <p class="contact-title">PRESIDENT</p>
  </div>
  <p class="contact-lines address">42 W. Calloway Blvd., Suite 300<br>Larkmont, CA 91847</p>
  <p class="contact-lines phones">O 555.555.0147 ext. 204<br>C 555.555.0192</p>
  <p class="contact-lines email">Email: russ@halveringpartnersgroup.com</p>

  <div class="wordmark">
    <span class="wordmark-square"></span>
    <span class="wordmark-name">Halvering</span>
    <span class="wordmark-sub">&amp; Partners</span>
  </div>
</section>

<section class="card card-back" aria-label="Card back">
  <svg class="card-art" viewBox="0 0 829 482" aria-hidden="true">
    <defs>
      <linearGradient id="backRed" x1="0" y1="0" x2="1" y2="0">
        <stop offset="0" stop-color="var(--deep-red)"/>
        <stop offset="0.35" stop-color="var(--bright-red)"/>
        <stop offset="0.7" stop-color="var(--frame-red)"/>
        <stop offset="1" stop-color="var(--bright-red)"/>
      </linearGradient>
    </defs>
    <rect width="829" height="482" fill="url(#backRed)"/>
    <path d="M7 7 H822 V410 C620 300 300 290 7 310 Z" fill="var(--panel-black)"/>
    <path d="M7 318 C300 300 560 310 822 420 V428 C560 330 300 312 7 328 Z" fill="#ff5a5a" opacity="0.55"/>
    <rect x="7" y="425" width="815" height="50" rx="4" fill="var(--panel-grey)"/>
  </svg>

  <div class="wordmark">
    <span class="wordmark-square"></span>
    <span class="wordmark-name">Halvering</span>
    <span class="wordmark-sub">&amp; Partners</span>
  </div>

  <p class="web-address">WWW.HALVERINGPARTNERSGROUP.COM</p>
</section>

</body>
</html>
```